Bramblewick Painting Epoxy Flyer

We need a promotional flyer for a new epoxy floor coatings division of our painting company. We do epoxy garage floor coatings and paver sealing. It needs to be based on and very similar to the attached flyer. The garage floor picture needs to look more realistic, and the before and after pavers pictures should look less shiny but still a good contrast. Include attached logo

```html
<!DOCTYPE html>
<html lang="en">
<head>
<meta charset="utf-8">
<title>Bramblewick Painting – Epoxy Flyer</title>
<link href="https://fonts.googleapis.com/css2?family=Poppins:ital,wght@0,400;0,500;0,600;0,700;0,800;1,300;1,500;1,700;1,800;1,900&display=swap" rel="stylesheet">
<style>
  :root{
    --bg:#e4e4e4;
    --paper:#ffffff;
    --blue:#2f86c6;
    --teal:#2aa59a;
    --green:#5fb23e;
    --orange:#d9621e;
    --rust:#b5481a;
    --ink:#1f1f1f;
    --text:#333333;
    --bar:#ececec;
  }
  *{margin:0;padding:0;box-sizing:border-box}
  html,body{width:1200px;height:706px;overflow:hidden}
  body{background:var(--bg);font-family:"Poppins",sans-serif;color:var(--text)}

  .flyer{position:absolute;left:367px;top:23px;width:466px;height:660px;background:var(--paper);overflow:hidden;box-shadow:0 4px 14px rgba(0,0,0,.18)}

  .hero-panel{position:absolute;left:170px;top:0;width:296px;height:232px;
    background:linear-gradient(180deg,var(--blue) 0%,var(--teal) 25%,var(--green) 48%,#8e8f2a 62%,var(--orange) 80%,var(--rust) 100%)}
  .headline{position:absolute;left:198px;top:14px;color:#fff;font-style:italic;line-height:1}
  .headline .lead{display:block;font-weight:300;font-size:33px;letter-spacing:.5px}
  .headline .big{display:block;font-weight:900;font-size:48px;margin-top:2px;letter-spacing:-.5px}
  .headline .amp{font-weight:500}
  .tagline{position:absolute;left:196px;top:146px;width:204px;height:21px;background:#fff;
    transform:skewX(-20deg);}
  .tagline span{display:block;transform:skewX(20deg);color:var(--orange);font-weight:600;font-size:13px;line-height:21px;padding-left:10px}

  .brand{position:absolute;left:0;top:84px;width:170px;text-align:center}
  .brand-dot{display:block;width:56px;height:56px;border-radius:50%;margin:0 auto 10px;
    background:linear-gradient(135deg,var(--blue),var(--green) 50%,var(--orange))}
  .brand-name{font-weight:600;font-size:12px;color:var(--ink);letter-spacing:.3px;line-height:1.3}

  .gallery{position:absolute;left:23px;top:188px;width:420px;display:grid;grid-template-columns:205px 205px;grid-template-rows:106px 106px;gap:12px 10px}
  .shot{position:relative;border-radius:7px;overflow:hidden}
  .shot .label{position:absolute;left:0;right:0;bottom:6px;text-align:center;color:#fff;font-weight:700;font-size:15px;text-shadow:0 1px 3px rgba(0,0,0,.6)}
  .shot::after{content:"";position:absolute;inset:0;background:linear-gradient(180deg,transparent 55%,rgba(0,0,0,.45))}
  .shot .label{z-index:1}
  .garage-before{background:linear-gradient(180deg,#8f7e69 0%,#bdb6aa 30%,#8d8a84 55%,#6b6964 100%)}
  .paver-before{background:linear-gradient(180deg,#4d5a3a 0%,#7a7060 25%,#8c8172 55%,#6d655a 100%)}
  .garage-after{background:linear-gradient(180deg,#8a6e52 0%,#d9d4cb 28%,#8d8d8d 50%,#555 80%,#3a3a3a 100%)}
  .paver-after{background:linear-gradient(180deg,#3f5a2c 0%,#6a4e33 30%,#8a5a35 60%,#5c3c24 100%)}

  .services{position:absolute;left:23px;top:422px;width:430px;display:flex}
  .service{width:217px}
  .service + .service{border-left:1.5px solid #d5d5d5;padding-left:22px;width:213px}
  .service h2{font-size:14px;font-weight:700;letter-spacing:-.1px;
    background:linear-gradient(90deg,var(--blue),var(--teal) 60%,var(--green));-webkit-background-clip:text;background-clip:text;color:transparent;margin-bottom:10px}
  .service ul{list-style:none}
  .service li{display:flex;align-items:center;gap:7px;font-size:9.6px;color:var(--text);height:16px}
  .tick{width:13px;height:13px;flex:none}

  .slogan{position:absolute;left:62px;top:527px;width:343px;height:21px;transform:skewX(-18deg);
    background:linear-gradient(90deg,var(--rust),var(--orange) 30%,var(--green) 65%,var(--blue))}
  .slogan span{display:block;transform:skewX(18deg);text-align:center;color:#fff;font-style:italic;font-weight:500;font-size:11px;line-height:21px}

  .trust{position:absolute;left:35px;top:564px;width:420px;display:flex;justify-content:space-between}
  .trust-item{display:flex;align-items:center;gap:9px;font-size:10.4px;line-height:1.2;color:var(--ink)}
  .trust-icon{width:20px;height:22px;flex:none}

  .contact-bar{position:absolute;left:0;top:599px;width:466px;height:48px;background:var(--bar)}
  .cta{position:absolute;left:0;top:602px;width:131px;height:45px;border-radius:0 6px 6px 0;
    background:linear-gradient(90deg,var(--rust),var(--orange) 45%,var(--green) 75%,var(--blue));
    color:#fff;font-weight:800;font-size:12.5px;line-height:1.05;padding:9px 0 0 22px}
  .phone{position:absolute;left:147px;top:604px;display:flex;align-items:center;gap:5px;font-weight:700;font-size:21px;color:var(--ink);letter-spacing:-.2px;line-height:1}
  .phone svg{width:15px;height:15px}
  .web{position:absolute;left:147px;top:629px;display:flex;align-items:center;gap:9px;font-size:9.4px;color:var(--ink)}
  .web svg{width:11px;height:11px}
  .promise{position:absolute;left:334px;top:602px;width:132px;height:45px;border-radius:6px 0 0 6px;
    background:linear-gradient(90deg,var(--blue),var(--teal) 30%,var(--green) 55%,var(--orange) 85%,var(--rust));
    color:#fff;font-weight:700;font-size:9px;line-height:1.2;padding:11px 0 0 11px}
</style>
</head>
<body>
<main class="flyer">
  <div class="hero-panel"></div>
  <h1 class="headline">
    <span class="lead">Upgrade Your</span>
    <span class="big">Garage <span class="amp">&amp;</span></span>
    <span class="big">Driveway</span>
  </h1>
  <div class="tagline"><span>From worn-out to like new</span></div>

  <div class="brand">
    <span class="brand-dot"></span>
    <div class="brand-name">Bramblewick Painting</div>
  </div>

  <section class="gallery">
    <figure class="shot garage-before" role="img" aria-label="Photo of a stained, worn concrete garage floor before coating"><span class="label">BEFORE</span></figure>
    <figure class="shot paver-before" role="img" aria-label="Photo of faded, weathered paver patio before sealing"><span class="label">BEFORE</span></figure>
    <figure class="shot garage-after" role="img" aria-label="Photo of garage floor with a new flake epoxy coating"><span class="label">AFTER</span></figure>
    <figure class="shot paver-after" role="img" aria-label="Photo of sealed pavers with restored warm colour"><span class="label">AFTER</span></figure>
  </section>

  <section class="services">
    <div class="service">
      <h2>EPOXY FLOOR COATINGS</h2>
      <ul>
        <li><svg class="tick" viewBox="0 0 14 14"><rect x="1" y="2" width="11" height="11" rx="1.5" fill="none" stroke="#d9621e" stroke-width="1.4"/><path d="M3.5 7.5l2.5 2.5 6.5-8" fill="none" stroke="#5fb23e" stroke-width="2" stroke-linecap="round"/></svg>Durable, long-lasting finish</li>
        <li><svg class="tick" viewBox="0 0 14 14"><rect x="1" y="2" width="11" height="11" rx="1.5" fill="none" stroke="#d9621e" stroke-width="1.4"/><path d="M3.5 7.5l2.5 2.5 6.5-8" fill="none" stroke="#5fb23e" stroke-width="2" stroke-linecap="round"/></svg>Slip-resistant texture</li>
        <li><svg class="tick" viewBox="0 0 14 14"><rect x="1" y="2" width="11" height="11" rx="1.5" fill="none" stroke="#d9621e" stroke-width="1.4"/><path d="M3.5 7.5l2.5 2.5 6.5-8" fill="none" stroke="#5fb23e" stroke-width="2" stroke-linecap="round"/></svg>Covers cracks &amp; imperfections</li>
        <li><svg class="tick" viewBox="0 0 14 14"><rect x="1" y="2" width="11" height="11" rx="1.5" fill="none" stroke="#d9621e" stroke-width="1.4"/><path d="M3.5 7.5l2.5 2.5 6.5-8" fill="none" stroke="#5fb23e" stroke-width="2" stroke-linecap="round"/></svg>Easy to clean &amp; maintain</li>
      </ul>
    </div>
    <div class="service">
      <h2>PAVER SEALING</h2>
      <ul>
        <li><svg class="tick" viewBox="0 0 14 14"><rect x="1" y="2" width="11" height="11" rx="1.5" fill="none" stroke="#d9621e" stroke-width="1.4"/><path d="M3.5 7.5l2.5 2.5 6.5-8" fill="none" stroke="#5fb23e" stroke-width="2" stroke-linecap="round"/></svg>Restores color &amp; enhances appearance</li>
        <li><svg class="tick" viewBox="0 0 14 14"><rect x="1" y="2" width="11" height="11" rx="1.5" fill="none" stroke="#d9621e" stroke-width="1.4"/><path d="M3.5 7.5l2.5 2.5 6.5-8" fill="none" stroke="#5fb23e" stroke-width="2" stroke-linecap="round"/></svg>Protects from sun fading</li>
        <li><svg class="tick" viewBox="0 0 14 14"><rect x="1" y="2" width="11" height="11" rx="1.5" fill="none" stroke="#d9621e" stroke-width="1.4"/><path d="M3.5 7.5l2.5 2.5 6.5-8" fill="none" stroke="#5fb23e" stroke-width="2" stroke-linecap="round"/></svg>Helps prevent weeds &amp; sand loss</li>
        <li><svg class="tick" viewBox="0 0 14 14"><rect x="1" y="2" width="11" height="11" rx="1.5" fill="none" stroke="#d9621e" stroke-width="1.4"/><path d="M3.5 7.5l2.5 2.5 6.5-8" fill="none" stroke="#5fb23e" stroke-width="2" stroke-linecap="round"/></svg>Easier to clean &amp; maintain</li>
      </ul>
    </div>
  </section>

  <div class="slogan"><span>Practical upgrades that protect and improve your home</span></div>

  <section class="trust">
    <div class="trust-item">
      <svg class="trust-icon" viewBox="0 0 20 22"><path d="M10 1l8 3v7c0 5-4 8.5-8 10C6 19.5 2 16 2 11V4z" fill="#2aa59a"/><rect x="6" y="7" width="8" height="2" fill="#fff"/><rect x="6" y="11" width="6" height="2" fill="#fff"/><circle cx="15" cy="16" r="3.2" fill="#d9621e"/></svg>
      <span>Licensed &amp;<br>Insured</span>
    </div>
    <div class="trust-item">
      <svg class="trust-icon" viewBox="0 0 20 22"><path d="M10 16C4 12 1 9 1 5.5 1 3 3 1 5.5 1 7.5 1 9 2.5 10 4c1-1.5 2.5-3 4.5-3C17 1 19 3 19 5.5 19 9 16 12 10 16z" fill="#2aa59a"/><circle cx="10" cy="7" r="2.5" fill="#fff"/><circle cx="5" cy="19" r="1.6" fill="#d9621e"/><circle cx="10" cy="20" r="1.6" fill="#d9621e"/><circle cx="15" cy="19" r="1.6" fill="#d9621e"/></svg>
      <span>Family-Owned<br>Local Business</span>
    </div>
    <div class="trust-item">
      <svg class="trust-icon" viewBox="0 0 20 22"><path d="M10 1a5 5 0 0 0-5 5c0 4 5 9 5 9s5-5 5-9a5 5 0 0 0-5-5z" fill="#2aa59a"/><circle cx="10" cy="6" r="2" fill="#fff"/><path d="M2 21l4-6h8l4 6z" fill="#d9621e"/></svg>
      <span>Serving Alderbrook &amp;<br>Surrounding Areas</span>
    </div>
  </section>

  <div class="contact-bar"></div>
  <div class="cta">CALL FOR A<br>FREE ESTIMATE</div>
  <div class="phone">
    <svg viewBox="0 0 16 16"><path d="M3.5 1l2.5 3-1.5 2c.8 2 2.5 3.7 4.5 4.5l2-1.5 3 2.5-1.5 2.5C7 14 2 9 1 2.5z" fill="#1f1f1f"/></svg>
    <span>555-014-2290</span>
  </div>
  <div class="web">
    <svg viewBox="0 0 12 12"><circle cx="6" cy="6" r="5.2" fill="none" stroke="#1f1f1f" stroke-width="1"/><ellipse cx="6" cy="6" rx="2.3" ry="5.2" fill="none" stroke="#1f1f1f" stroke-width="1"/><path d="M1 6h10M1.8 3.5h8.4M1.8 8.5h8.4" stroke="#1f1f1f" stroke-width=".8"/></svg>
    <span>www.bramblewickpainting.com</span>
  </div>
  <div class="promise">Fast, professional<br>service you can trust</div>
</main>
</body>
</html>
```